Commercial HVAC and Refrigeration Business cards

Frost-Haven Company is looking for flashy new business cards! We design, install, service and maintain commercial refrigeration, air conditioning, heating and refrigeration equipment. Our colors are blue and white. I'm open to single and double sided designs. Each employee will have their own business card. I've attached a copy of our current logo.

Our website, office and cell phone (cell phone is optional), email address should be clearly legible. "24 Hour Service" and the services we offer are; Sales, Service, Design, Installation, Maintenance. Refrigeration, Heating, Air Conditioning, Ice Machines. Does not have to be in any order.

Target Market(s)

Commercial; Restaurants, hotels, bars, breweries etc.

Industry/Entity Type

Hvac

Contact Information for Business Card

Name; Job Title, Phone Number, Email Address. www.frost-haven-example.com 24 Hour Service. We provide - Sales, Design, Installation, Service, Maintenance. We service - Refrigeration, Heating, Air Conditioning, Ice Machines

Font styles to use
Other font styles liked:
• Be creative

Colors
0255a3
ffffff

Requirements
Must have
• Professional appearance and appeal to commercial clients in the food-service and hospitality industry. Must be clearly legible and easy to understand.
Nice to have
• We want to sell maintenance agreements, perhaps we can use the back of the card to tie into a webpage about our maintenance agreements.
Should not have
• Cartoons or unprofessional. Nothing too edgy.

```html
<!DOCTYPE html>
<html lang="en">
<head>
<meta charset="utf-8">
<title>Frost-Haven Company – Business Card</title>
<link rel="stylesheet" href="https://fonts.googleapis.com/css2?family=Open+Sans:wght@400;600&display=swap">
<style>
  :root {
    --page-bg: #e9eaec;
    --card-bg: #111214;
    --brand-blue: #0255a3;
    --accent-blue: #1d6fd0;
    --text-white: #ffffff;
    --text-grey: #8a8d92;
    --card-edge: #b88a55;
  }
  * { margin: 0; padding: 0; box-sizing: border-box; }
  html, body {
    width: 1200px; height: 1000px; overflow: hidden;
    background: var(--page-bg);
    font-family: "Open Sans", Arial, sans-serif;
  }
  .card {
    position: absolute; left: 100px; top: 214px;
    width: 1000px; height: 572px;
    background: var(--card-bg);
    border-radius: 6px;
    box-shadow: 0 0 0 3px var(--card-edge), 0 18px 40px rgba(0,0,0,.25);
    color: var(--text-white);
  }
  .card > * { position: absolute; white-space: nowrap; }
  .offer-heading {
    left: 60px; top: 36px;
    color: var(--accent-blue); font-size: 28px; font-weight: 400; letter-spacing: .5px; line-height: 40px;
  }
  .group-title { color: var(--accent-blue); font-size: 26px; font-weight: 400; line-height: 36px; }
  .provide-title { left: 60px; top: 80px; }
  .service-title { left: 330px; top: 140px; }
  .service-list { list-style: none; font-size: 21px; line-height: 29px; }
  .service-list li::before {
    content: ""; display: inline-block; width: 6px; height: 6px; border-radius: 50%;
    background: var(--accent-blue); margin-right: 10px; vertical-align: middle;
  }
  .provide-list { left: 60px; top: 118px; }
  .service-list.repairs { left: 330px; top: 178px; }
  .person {
    left: 60px; top: 318px; font-size: 32px; line-height: 46px; color: var(--accent-blue); font-weight: 400;
  }
  .person .role { color: var(--text-grey); font-size: 26px; }
  .divider { height: 2px; background: var(--brand-blue); }
  .divider.name-rule { left: 60px; top: 370px; width: 500px; }
  .divider.web-rule { right: 50px; top: 524px; width: 380px; }
  .contact { display: flex; align-items: center; gap: 14px; font-size: 22px; line-height: 32px; }
  .contact svg { width: 22px; height: 22px; flex: none; }
  .contact.phone { left: 60px; top: 390px; }
  .contact.email { left: 230px; top: 436px; }
  .contact.web { right: 50px; top: 484px; }
  .brand {
    left: 620px; top: 190px; width: 330px; height: 120px;
    display: flex; align-items: center; gap: 16px;
  }
  .brand-mark { width: 26px; height: 26px; background: var(--accent-blue); flex: none; }
  .brand-name { font-size: 32px; font-weight: 600; color: var(--text-white); line-height: 1.15; white-space: normal; }
  .hours { left: 662px; top: 322px; color: var(--accent-blue); font-size: 22px; line-height: 32px; }
</style>
</head>
<body>
  <main class="card">
    <h2 class="offer-heading">MAINTENANCE AGREEMENTS</h2>

    <h3 class="group-title provide-title">We provide</h3>
    <ul class="service-list provide-list">
      <li>Sales</li><li>Design</li><li>Installation</li><li>Service</li><li>Maintenance</li>
    </ul>

    <h3 class="group-title service-title">We service</h3>
    <ul class="service-list repairs">
      <li>Refrigeration</li><li>Heating</li><li>Air Conditioning</li><li>Ice Machines</li>
    </ul>

    <p class="person">Daniel Reyes - <span class="role">CEO/Founder</span></p>
    <div class="divider name-rule"></div>

    <p class="contact phone">
      <svg viewBox="0 0 24 24" aria-hidden="true"><path fill="#1d6fd0" d="M6.6 10.8a15.1 15.1 0 0 0 6.6 6.6l2.2-2.2a1 1 0 0 1 1-.25 11.4 11.4 0 0 0 3.6.57 1 1 0 0 1 1 1V20a1 1 0 0 1-1 1A17 17 0 0 1 3 4a1 1 0 0 1 1-1h3.5a1 1 0 0 1 1 1c0 1.25.2 2.45.57 3.57a1 1 0 0 1-.25 1z"/></svg>
      555 014 2276
    </p>
    <p class="contact email">
      <svg viewBox="0 0 24 24" aria-hidden="true"><rect x="2" y="5" width="20" height="14" rx="1.5" fill="#1d6fd0"/><path d="M3 6l9 7 9-7" fill="none" stroke="#111214" stroke-width="1.6"/></svg>
      daniel@frost-haven-example.com
    </p>

    <div class="brand">
      <span class="brand-mark"></span>
      <span class="brand-name">Frost-Haven Company</span>
    </div>
    <p class="hours">24 Hour Service</p>

    <p class="contact web">
      <svg viewBox="0 0 24 24" aria-hidden="true"><circle cx="12" cy="12" r="10" fill="#1d6fd0"/><path d="M2 12h20M12 2c3 3 3 17 0 20M12 2c-3 3-3 17 0 20" fill="none" stroke="#111214" stroke-width="1.4"/></svg>
      www.frost-haven-example.com
    </p>
    <div class="divider web-rule"></div>
  </main>
</body>
</html>
```